Dental specialist needs a sharp looking letterhead

I am looking for a letterhead to be used to send letters and communication between myself (a dental specialist) and other dentists.
My office is a state of the art dental specialty office.
I need to letterhead to also state:
Gideon R. Whitfield DDS
2847 Birchmont Avenue, Suite K
West Harlow, NY 14391
(716)482-9163
fax: (716)482-9170
whitfieldroot.com (**this email address may change)

i included my logo designs.
thank you

Target Market(s)

dentists

Industry/Entity Type

Communication

Requirements
Must have
• the included logo, whether the vertical or horizontal versions

```html
<!DOCTYPE html>
<html lang="en">
<head>
<meta charset="utf-8">
<title>Keystone Endodontics P.C. – Letterhead</title>
<link rel="stylesheet" href="https://fonts.googleapis.com/css2?family=Kreon:wght@400&display=swap">
<style>
  :root {
    --backdrop: #d2ad72;
    --paper: #fbfbfb;
    --header-bg: #0c0b0a;
    --header-text: #ffffff;
    --accent-blue: #3b9bd8;
    --accent-green: #8cc21f;
    --divider: #6b6b6b;
  }
  * { margin: 0; padding: 0; box-sizing: border-box; }
  html, body {
    width: 898px;
    height: 1200px;
    overflow: hidden;
    background: var(--backdrop);
    font-family: "Kreon", Georgia, serif;
  }
  .sheet {
    position: absolute;
    left: 65px;
    top: 46px;
    width: 768px;
    height: 1087px;
    background: var(--paper);
  }
  .letterhead-header {
    position: relative;
    height: 127px;
    background: var(--header-bg);
    color: var(--header-text);
  }
  .accent-rule {
    height: 7px;
    background: linear-gradient(to bottom, var(--accent-green) 0 2px, var(--header-bg) 2px 3px, var(--accent-blue) 3px 5px, var(--accent-green) 5px 7px);
  }
  .brand {
    position: absolute;
    left: 26px;
    top: 28px;
    display: flex;
    align-items: center;
    gap: 14px;
  }
  .brand-mark {
    width: 56px;
    height: 56px;
    border-radius: 50%;
    background: var(--accent-blue);
  }
  .brand-divider {
    width: 1px;
    height: 88px;
    background: var(--divider);
  }
  .brand-name {
    color: var(--header-text);
    font-weight: 400;
    line-height: 1;
  }
  .brand-name .primary {
    display: block;
    font-size: 37px;
    letter-spacing: 0.5px;
  }
  .brand-name .secondary {
    display: block;
    font-size: 15px;
    letter-spacing: 2.4px;
    margin-top: 6px;
    padding-left: 26px;
  }
  .contact {
    position: absolute;
    right: 25px;
    top: 44px;
    text-align: right;
    font-size: 13px;
    line-height: 1;
  }
  .contact .doctor {
    font-size: 18px;
    margin-top: -2px;
    margin-bottom: 15px;
  }
  .contact-line {
    display: flex;
    justify-content: flex-end;
    align-items: center;
    gap: 5px;
    margin-bottom: 11px;
  }
  .contact-line .gap { width: 12px; }
  .icon { width: 11px; height: 11px; fill: var(--header-text); }
  .letterhead-footer {
    position: absolute;
    left: 0;
    right: 0;
    top: 1038px;
    display: flex;
    justify-content: center;
    align-items: center;
    gap: 8px;
    font-size: 13px;
    padding-left: 16px;
  }
  .footer-email { color: var(--accent-blue); display: flex; align-items: center; gap: 5px; }
  .footer-web { color: var(--accent-green); display: flex; align-items: center; gap: 5px; }
  .footer-divider { width: 1px; height: 30px; background: var(--divider); }
  .footer-email .icon { fill: var(--accent-blue); }
  .footer-web .icon { fill: none; stroke: var(--accent-green); stroke-width: 1.3; }
</style>
</head>
<body>
  <div class="sheet">
    <header class="letterhead-header">
      <div class="brand">
        <div class="brand-mark"></div>
        <div class="brand-divider"></div>
        <div class="brand-name">
          <span class="primary">KEYSTONE</span>
          <span class="secondary">Endodontics P.C.</span>
        </div>
      </div>
      <div class="contact">
        <div class="doctor">Gideon R. Whitfield DDS</div>
        <div class="contact-line">
          <svg class="icon" viewBox="0 0 12 12" aria-hidden="true"><circle cx="6" cy="6" r="6"/><path d="M4 3.2c.4-.2.8 0 .9.4l.2.8-.6.5c.3.8.9 1.4 1.6 1.7l.5-.6.8.2c.4.1.6.5.4.9-.3.6-1 .8-1.7.5C4.8 7 4 6 3.6 4.8c-.2-.7 0-1.3.4-1.6z" fill="#0c0b0a"/></svg>
          <span>(716) 482 9163</span>
          <span class="gap"></span>
          <svg class="icon" viewBox="0 0 12 12" aria-hidden="true"><circle cx="6" cy="6" r="6"/><rect x="3.5" y="2.8" width="5" height="2" fill="#0c0b0a"/><rect x="2.8" y="5.2" width="6.4" height="3.4" rx=".6" fill="#0c0b0a"/></svg>
          <span>(716) 482 9170</span>
        </div>
        <div class="contact-line">
          <svg class="icon" viewBox="0 0 12 12" aria-hidden="true"><circle cx="6" cy="6" r="6"/><path d="M6 2.5a2.3 2.3 0 0 0-2.3 2.3C3.7 6.6 6 9.5 6 9.5s2.3-2.9 2.3-4.7A2.3 2.3 0 0 0 6 2.5zm0 3.2a.9.9 0 1 1 0-1.8.9.9 0 0 1 0 1.8z" fill="#0c0b0a"/></svg>
          <span>2847 Birchmont Avenue, Suite K, West Harlow, NY 14391</span>
        </div>
      </div>
    </header>
    <div class="accent-rule"></div>

    <footer class="letterhead-footer">
      <span class="footer-email">
        <svg class="icon" viewBox="0 0 12 12" aria-hidden="true"><path d="M6 0a6 6 0 1 0 0 12A6 6 0 0 0 6 0zm3 8.5H3v-5h6v5zM3.4 4 6 6.2 8.6 4z"/></svg>
        gideon@whitfieldroot.com
      </span>
      <span class="footer-divider"></span>
      <span class="footer-web">
        <svg class="icon" viewBox="0 0 12 12" aria-hidden="true"><circle cx="6" cy="6" r="5.3"/><ellipse cx="6" cy="6" rx="2.4" ry="5.3"/><path d="M.7 6h10.6M1.6 3.3h8.8M1.6 8.7h8.8"/></svg>
        www.whitfieldroot.com
      </span>
    </footer>
  </div>
</body>
</html>
```